Zerovan Medical

We are a medical supplier company we sell machines and equipment to all medical sectors in Iraq. Our services include not only the installation of these machines and equipment but also we provide support after installation and we train the staff to use these machines/equipment
We need a website that will make us stand out from our competitors, something professional and catchy
Starting from the home page, before showing the home page we want the loading screen to have our logo animated in a nice way
Then we can proceed to creating the other pages which are
Projects
Services
Training
About
and Contact us
Attached below is our logo and the color blue that we hope to use in the theme of the website
**** In the home page we want to focus on our partners and services****

Target Market(s)

Medical Sector

Industry/Entity Type

Medical

Coding

Coded - Design and coding required

Number of Pages Required

5+ page

Colors
0054AA
0677BA
7BADD7
CADEEF
E8F1F8

Requirements
Must have
• Animation in loading screen or animation in home page
Nice to have
• Some sort of animation for our partners

```html
<!DOCTYPE html>
<html lang="en">
<head>
<meta charset="utf-8">
<title>Zerovan Medical</title>
<link href="https://fonts.googleapis.com/css2?family=Open+Sans:wght@400;600;700;800&display=swap" rel="stylesheet">
<style>
:root{
  --blue:#0677BA;
  --blue-dark:#0054AA;
  --blue-mid:#7BADD7;
  --blue-pale:#CADEEF;
  --blue-tint:#E8F1F8;
  --ink:#111820;
  --text:#333;
  --muted:#666;
  --footer:#0b1826;
  --white:#fff;
}
*{margin:0;padding:0;box-sizing:border-box}
html,body{width:1200px;height:3584px;overflow:hidden}
body{font-family:"Open Sans",sans-serif;color:var(--text);background:var(--white);position:relative}
.abs{position:absolute}
.btn{position:absolute;display:flex;align-items:center;justify-content:center;background:var(--blue);color:var(--white);border-radius:30px;font-size:13px;font-weight:600;text-decoration:none}
.section-title{position:absolute;left:0;width:1200px;text-align:center;font-weight:700;font-size:36px;color:var(--ink)}

/* header */
.header{position:absolute;top:0;left:0;width:1200px;height:91px;background:var(--white)}
.brand{position:absolute;left:141px;top:26px;display:flex;align-items:center;gap:12px}
.brand-mark{width:40px;height:40px;border:4px solid var(--blue)}
.brand-name{font-size:32px;font-weight:700;color:#1d2a5a}
.nav{position:absolute;top:34px;font-size:13px;color:var(--ink)}
.nav.active{color:var(--blue);font-weight:600}

/* hero */
.hero{position:absolute;top:91px;left:0;width:1200px;height:531px;background:linear-gradient(180deg,#3e5a78 0%,#2d4b6c 50%,#243f5e 100%)}
.hero-title{position:absolute;top:215px;width:1200px;text-align:center;color:var(--white);font-size:44px;font-weight:700;letter-spacing:1px}
.hero-sub{position:absolute;top:286px;width:1200px;text-align:center;color:var(--white);font-size:17px}

/* partners */
.partner{position:absolute;top:805px;height:60px;width:150px;border-radius:8px;background:var(--blue-tint)}

/* about */
.about{position:absolute;top:967px;left:0;width:1200px;height:529px;background:var(--blue-tint)}
.about-photo{position:absolute;left:142px;top:64px;width:433px;height:403px;background:linear-gradient(160deg,#e9eef2,#c6ced6)}
.about-label{position:absolute;left:629px;top:94px;font-size:17px;color:#1d2a5a}
.about-heading{position:absolute;left:629px;top:124px;font-size:21px;font-weight:700;color:var(--ink)}
.about-text{position:absolute;left:629px;width:440px;font-size:13px;line-height:22.5px;color:var(--text)}

/* services */
.service{position:absolute;top:1663px;width:293px;height:311px;background:var(--blue-tint);border-radius:24px 24px 0 70px;text-align:center}
.service.featured{background:var(--blue);color:var(--white)}
.service-icon{position:absolute;left:98px;top:46px;width:96px;height:96px;border-radius:50%;background:var(--blue);display:flex;align-items:center;justify-content:center}
.service.featured .service-icon{background:var(--white)}
.service h3{position:absolute;top:163px;width:100%;font-size:18px;font-weight:700;color:var(--ink)}
.service.featured h3{color:var(--white)}
.service p{position:absolute;top:194px;left:36px;width:221px;font-size:11.5px;line-height:19px}
.service a{position:absolute;top:262px;width:100%;left:0;font-size:13px;color:var(--blue);text-decoration:underline}
.service.featured a{color:var(--white)}

/* testimonials */
.review{position:absolute;top:2151px;width:427px;height:240px;background:#f6f6f6;border-radius:8px}
.review.raised{background:var(--white);box-shadow:0 2px 14px rgba(0,0,0,.08)}
.avatar{position:absolute;left:18px;top:34px;width:58px;height:58px;border-radius:50%;background:linear-gradient(135deg,#c9a58f,#7a5a48)}
.stars{position:absolute;left:92px;top:30px;color:#f5b400;font-size:14px;letter-spacing:1px}
.review-name{position:absolute;left:92px;top:46px;font-size:23px;font-weight:600;color:#1d2a3a}
.review-role{position:absolute;left:92px;top:78px;font-size:15px;color:var(--muted)}
.review-text{position:absolute;left:92px;top:112px;width:310px;font-size:14px;line-height:23px;color:var(--muted)}
.review-badge{position:absolute;right:40px;top:30px;width:30px;height:30px;border-radius:50%;background:#e2e6ea}
.arrow-btn{position:absolute;left:62px;top:2244px;width:52px;height:52px;border-radius:50%;border:1.5px solid #333;background:var(--white);display:flex;align-items:center;justify-content:center}

/* projects */
.project{position:absolute;top:2559px;width:294px;height:244px}
.project-caption{position:absolute;bottom:22px;left:0;width:100%;text-align:center;color:var(--white);font-size:12px;font-weight:600;line-height:20px}

/* cta */
.cta{position:absolute;top:2996px;left:0;width:1200px;height:275px;background:linear-gradient(180deg,#1a7fc4,#0d6fb4)}
.cta h2{position:absolute;top:48px;width:1200px;text-align:center;color:var(--white);font-size:37px;font-weight:700;line-height:46px}

/* footer */
.footer{position:absolute;top:3271px;left:0;width:1200px;height:313px;background:var(--footer);color:var(--white)}
.foot-nav{position:absolute;top:62px;font-size:13px}
.foot-nav.active{color:#3d8fd6}
.foot-rule{position:absolute;left:141px;width:918px;height:1px;background:#2c3b4d}
.foot-sep{position:absolute;top:107px;width:1px;height:72px;background:#2c3b4d}
.foot-info{position:absolute;top:128px;font-size:13px;line-height:22px}
.social{position:absolute;top:272px;width:22px;height:22px;border-radius:50%;background:var(--blue)}
</style>
</head>
<body>

<header class="header">
  <div class="brand"><div class="brand-mark"></div><span class="brand-name">Zerovan</span></div>
  <span class="nav active" style="left:511px">Home</span>
  <span class="nav" style="left:573px">About Us</span>
  <span class="nav" style="left:654px">Services</span>
  <span class="nav" style="left:728px">Featured Projects</span>
  <span class="nav" style="left:860px">Training</span>
  <a class="btn" style="left:933px;top:22px;width:125px;height:42px">Contact Us</a>
</header>

<section class="hero" role="img" aria-label="Operating room with medical equipment under blue tint">
  <h1 class="hero-title">EMPOWERING MEDICAL EXCELLENCE</h1>
  <p class="hero-sub">Your trusted partner for medical equipment and services</p>
  <a class="btn" style="left:537px;top:341px;width:126px;height:43px">Learn More</a>
  <svg class="abs" style="left:586px;top:438px" width="28" height="34" viewBox="0 0 28 34" fill="none" stroke="#fff" stroke-width="2" stroke-linecap="round" stroke-linejoin="round">
    <path d="M10 4v16M18 4v16M10 4a4 4 0 0 1 8 0M4 18l10 12 10-12"/>
  </svg>
</section>

<h2 class="section-title" style="top:698px">Our Partner</h2>
<div class="partner" style="left:137px"></div>
<div class="partner" style="left:340px"></div>
<div class="partner" style="left:526px"></div>
<div class="partner" style="left:712px"></div>
<div class="partner" style="left:911px"></div>

<section class="about">
  <div class="about-photo" role="img" aria-label="Bright operating theatre with surgical table and monitors"></div>
  <p class="about-label">About Us</p>
  <h2 class="about-heading">Zerovan Medical Equipments Suppliers</h2>
  <p class="about-text" style="top:166px">Lorem ipsum dolor sit amet, consectetur adipiscing elit, sed do eiusmod tempor incididunt ut labore et dolore magna aliqua. Quis ipsum suspendisse ultrices gravida. Risus commodo viverra maecenas accumsan lacus vel facilisis</p>
  <p class="about-text" style="top:279px">Lorem ipsum dolor sit amet, consectetur adipiscing elit, sed do eiusmod tempor incididunt ut labore et dolore magna aliqua. Quis ipsum suspendisse ultrices gravida. Risus commodo viverra maecenas accumsan lacus vel facilisis.</p>
  <a class="btn" style="left:629px;top:390px;width:125px;height:39px">Learn More</a>
</section>

<h2 class="section-title" style="top:1575px">Our Services</h2>
<article class="service" style="left:141px">
  <div class="service-icon">
    <svg width="46" height="46" viewBox="0 0 24 24" fill="none" stroke="#fff" stroke-width="1.6" stroke-linecap="round"><path d="M6 3v5a4 4 0 0 0 8 0V3M10 12v3a5 5 0 0 0 10 0v-2"/><circle cx="20" cy="11" r="2"/></svg>
  </div>
  <h3>Stethoscope</h3>
  <p>Lorem ipsum dolor sit amet, consectetur adipiscing elit, sed do eiusmod incididunt ut labore.</p>
  <a>Read More</a>
</article>
<article class="service featured" style="left:452px">
  <div class="service-icon">
    <svg width="46" height="46" viewBox="0 0 24 24" fill="none" stroke="#0677BA" stroke-width="1.6" stroke-linecap="round" stroke-linejoin="round"><circle cx="12" cy="12" r="3.5"/><path d="M12 2v3M12 19v3M2 12h3M19 12h3M4.9 4.9l2.1 2.1M17 17l2.1 2.1M4.9 19.1 7 17M17 7l2.1-2.1"/></svg>
  </div>
  <h3>Wrench</h3>
  <p>Lorem ipsum dolor sit amet, consectetur adipiscing elit, sed do eiusmod incididunt ut labore.</p>
  <a>Read More</a>
</article>
<article class="service" style="left:766px">
  <div class="service-icon">
    <svg width="46" height="46" viewBox="0 0 24 24" fill="none" stroke="#fff" stroke-width="1.6" stroke-linejoin="round"><path d="M12 6C9 4 5 4 2 5v14c3-1 7-1 10 1 3-2 7-2 10-1V5c-3-1-7-1-10 1zM12 6v14"/></svg>
  </div>
  <h3>Book</h3>
  <p>Lorem ipsum dolor sit amet, consectetur adipiscing elit, sed do eiusmod incididunt ut labore.</p>
  <a>Read More</a>
</article>

<h2 class="section-title" style="top:2053px">What Client Say About Us</h2>
<div class="arrow-btn">
  <svg width="20" height="14" viewBox="0 0 20 14" fill="none" stroke="#222" stroke-width="1.8" stroke-linecap="round" stroke-linejoin="round"><path d="M19 7H2M7 1 1 7l6 6"/></svg>
</div>
<article class="review raised" style="left:174px">
  <div class="avatar" role="img" aria-label="Client portrait"></div>
  <div class="stars">★★★★★</div>
  <div class="review-badge"></div>
  <p class="review-name">Daniel Ferrow</p>
  <p class="review-role">Client Profession</p>
  <p class="review-text">Lorem ipsum dolor sit amet, consectetur ip-sadipss isicing elit, sed do eiusmod tempor i ncidi dunt labore et dolore magna aliqua. sss Ut enim adispgd minim veniam,</p>
</article>
<article class="review" style="left:635px">
  <div class="avatar" role="img" aria-label="Client portrait"></div>
  <div class="stars">★★★★★</div>
  <div class="review-badge"></div>
  <p class="review-name">Daniel Ferrow</p>
  <p class="review-role">Client Profession</p>
  <p class="review-text">Lorem ipsum dolor sit amet, consectetur ip-sadipss isicing elit, sed do eiusmod tempor i ncidi dunt labore et dolore magna aliqua. sss Ut enim adispgd minim veniam,</p>
</article>
<article class="review" style="left:1093px">
  <div class="avatar" role="img" aria-label="Client portrait"></div>
  <div class="stars">★★★★★</div>
  <p class="review-name">Daniel Ferrow</p>
  <p class="review-role">Client Profession</p>
  <p class="review-text">Lorem ipsum dolor sit amet, consectetur ip-sadipss isicing elit, sed do eiusmod tempor i ncidi dunt labore et dolore magna aliqua. sss Ut enim adispgd minim veniam,</p>
</article>

<h2 class="section-title" style="top:2470px">Featured Projects</h2>
<figure class="project" style="left:142px;background:linear-gradient(180deg,#6fa0c8 0%,#3f6d92 60%,#1f3346 100%)" role="img" aria-label="Technician with patient at a scanner">
  <figcaption class="project-caption">Lorem ipsum dolor sit amet, consectetur<br>incididunt ut labore et.</figcaption>
</figure>
<figure class="project" style="left:453px;background:linear-gradient(180deg,#9fb6c8 0%,#5f7a90 60%,#24323f 100%)" role="img" aria-label="Laboratory microscope on a bench">
  <figcaption class="project-caption">Lorem ipsum dolor sit amet, consectetur<br>incididunt ut labore et.</figcaption>
</figure>
<figure class="project" style="left:764px;background:linear-gradient(160deg,#7f9cc2 0%,#4f6c8e 60%,#23303e 100%)" role="img" aria-label="Equipped clinical treatment room">
  <figcaption class="project-caption">Lorem ipsum dolor sit amet, consectetur<br>incididunt ut labore et.</figcaption>
</figure>
<a class="btn" style="left:507px;top:2854px;width:186px;height:50px;font-size:15px">View All products</a>

<section class="cta" role="img" aria-label="Blue-tinted medical equipment backdrop">
  <h2>Zerovan Medical Equipments<br>Suppliers</h2>
  <a class="btn" style="left:529px;top:170px;width:142px;height:40px;background:#fff;color:var(--blue)">Contact Now</a>
</section>

<footer class="footer">
  <span class="foot-nav active" style="left:325px">Home</span>
  <span class="foot-nav" style="left:398px">Services</span>
  <span class="foot-nav" style="left:485px">About Us</span>
  <span class="foot-nav" style="left:578px">Featured Projects</span>
  <span class="foot-nav" style="left:722px">Training</span>
  <span class="foot-nav" style="left:808px">Contact Us</span>
  <div class="foot-rule" style="top:98px"></div>

  <div class="abs" style="left:137px;top:150px;display:flex;align-items:center;gap:12px">
    <div style="width:40px;height:40px;border:4px solid #fff"></div>
    <span style="font-size:32px;font-weight:700">Zerovan</span>
  </div>
  <div class="foot-sep" style="left:388px"></div>
  <svg class="abs" style="left:418px;top:130px" width="16" height="18" viewBox="0 0 16 18" fill="none" stroke="#fff" stroke-width="1.5"><path d="M8 17s6-5.5 6-10A6 6 0 0 0 2 7c0 4.5 6 10 6 10z"/><circle cx="8" cy="7" r="2"/></svg>
  <p class="foot-info" style="left:444px">123 Lorem ipsume Dilor<br>Site 32311 Lorem ipsume</p>
  <div class="foot-sep" style="left:632px"></div>
  <svg class="abs" style="left:663px;top:132px" width="18" height="18" viewBox="0 0 24 24" fill="none" stroke="#fff" stroke-width="1.6" stroke-linejoin="round"><path d="M5 3h4l2 5-2.5 1.5a11 11 0 0 0 6 6L16 13l5 2v4a2 2 0 0 1-2 2A16 16 0 0 1 3 5a2 2 0 0 1 2-2z"/></svg>
  <p class="foot-info" style="left:696px">Call :<br>123 456 7890</p>
  <div class="foot-sep" style="left:812px"></div>
  <svg class="abs" style="left:845px;top:133px" width="18" height="14" viewBox="0 0 18 14" fill="none" stroke="#fff" stroke-width="1.5"><rect x="1" y="1" width="16" height="12" rx="1"/><path d="M1 2l8 6 8-6"/></svg>
  <p class="foot-info" style="left:878px">Email :<br>info@zerovanmedical.com</p>

  <div class="foot-rule" style="top:248px"></div>
  <p class="abs" style="left:141px;top:272px;font-size:12.5px">© 2024 Zerovan Medical Equipments Suppliers. All Rights Reserved.</p>
  <span class="social" style="left:975px"></span>
  <span class="social" style="left:1005px"></span>
  <span class="social" style="left:1036px"></span>
</footer>

</body>
</html>
```